Store Promo Card (already have logo!)

I need a card design (single side) for my online women’s gift shop containing a promotional code to be placed in bags for attendees at an event. I’m flexible on both shape and sizing, but perhaps a 4x6 card.
—It should contain my attached logo, my website (www.merrowlyn.com), and my Instagram handle (@merrowlyn) and promotion language such as “15% off your purchase with code: PIVRAL”.
—I think I would like my logo to be large.
—It should be clean, simple and modern in design and should use the colors from my logo.
—I would like about 3-5 product pictures depending on design.
Target Market(s)
Women ages 30 to 60
Industry/Entity Type
Retail Upscale Gift

```html
<!DOCTYPE html>
<html lang="en">
<head>
<meta charset="utf-8">
<title>Merrowlyn Promo Card</title>
<link rel="stylesheet" href="https://fonts.googleapis.com/css2?family=Arimo:wght@400;700&family=Jost:wght@400;500&display=swap">
<style>
  :root {
    --page: #ffffff;
    --blush: #e9d0c9;
    --ink: #5a5858;
    --coral: #e0907c;
    --white: #ffffff;
  }
  html, body {
    margin: 0;
    padding: 0;
    width: 1200px;
    height: 1000px;
    overflow: hidden;
    background: var(--page);
  }
  .canvas {
    position: relative;
    width: 1200px;
    height: 1000px;
  }
  .card {
    position: absolute;
    left: 283px;
    top: 22px;
    width: 635px;
    height: 954px;
    background: var(--blush);
  }
  .brand-name {
    position: absolute;
    left: 0;
    top: 74px;
    width: 100%;
    margin: 0;
    text-align: center;
    font-family: "Jost", sans-serif;
    font-weight: 500;
    font-size: 54px;
    letter-spacing: 2px;
    line-height: 1;
    color: var(--ink);
  }
  .tagline {
    position: absolute;
    left: 0;
    top: 166px;
    width: 100%;
    margin: 0;
    text-align: center;
    font-family: "Arimo", sans-serif;
    font-size: 22px;
    letter-spacing: 0.3px;
    color: var(--ink);
  }
  .product {
    position: absolute;
  }
  .product-tray {
    left: 32px; top: 218px; width: 305px; height: 305px;
    background: radial-gradient(ellipse at 50% 45%, #d2b57a 0%, #b99a5c 45%, #e9e7ea 72%);
  }
  .product-earrings {
    left: 337px; top: 218px; width: 255px; height: 305px;
    background: radial-gradient(circle at 50% 50%, #e3c57d 0%, #f6efe0 30%, #fbfafa 60%);
  }
  .product-slippers {
    left: 32px; top: 524px; width: 305px; height: 306px;
    background: radial-gradient(ellipse at 50% 55%, #e2cfc0 0%, #a8979f 40%, #f3f2f3 75%);
  }
  .offer {
    position: absolute;
    left: 356px;
    top: 546px;
    width: 231px;
    height: 279px;
    border: 2px solid var(--white);
    font-family: "Arimo", sans-serif;
  }
  .offer-amount {
    position: absolute;
    left: 12px;
    top: 66px;
    font-weight: 700;
    font-size: 104px;
    line-height: 1;
    letter-spacing: -3px;
    color: var(--coral);
  }
  .offer-percent {
    position: absolute;
    left: 145px;
    top: 74px;
    font-weight: 700;
    font-size: 52px;
    line-height: 1;
    color: var(--coral);
  }
  .offer-off {
    position: absolute;
    left: 137px;
    top: 128px;
    font-weight: 700;
    font-size: 34px;
    line-height: 1;
    color: var(--ink);
  }
  .offer-code {
    position: absolute;
    left: 0;
    top: 176px;
    width: 100%;
    text-align: center;
    font-size: 20px;
    color: var(--ink);
  }
  .contact {
    position: absolute;
    left: 0;
    width: 100%;
    margin: 0;
    text-align: center;
    font-family: "Jost", sans-serif;
    font-size: 27px;
    letter-spacing: 1px;
    color: var(--ink);
  }
  .contact-web { top: 855px; }
  .contact-social { top: 895px; }
</style>
</head>
<body>
<div class="canvas">
  <section class="card">
    <h1 class="brand-name">MERROWLYN</h1>
    <p class="tagline">Make Your Life Beautiful</p>

    <div class="product product-tray" role="img" aria-label="Product photo: round gold tray with leopard print"></div>
    <div class="product product-earrings" role="img" aria-label="Product photo: gold flower stud earrings with crystals"></div>
    <div class="product product-slippers" role="img" aria-label="Product photo: lavender slippers with blush pom-poms"></div>

    <div class="offer">
      <span class="offer-amount">15</span>
      <span class="offer-percent">%</span>
      <span class="offer-off">OFF</span>
      <span class="offer-code">with code: PIVRAL</span>
    </div>

    <p class="contact contact-web">www.merrowlyn.com</p>
    <p class="contact contact-social">@merrowlyn</p>
  </section>
</div>
</body>
</html>
```